Round Label Sticker 2.5-3 inch diameter

We need a design for a sticker to distribute for more brand recognition and product outreach.
My company The Bright Plate Company Ltd. Specializes in working with people with diabetes. My products are made for diabetics because they have no added sugars, high in protein and fiber and each serving is lower than 5% daily value of carbohydrates.
I am a dietitian and my dad passed away from diabetes. I have created a growing food and beverage line that will give more joy into a diabetic's life while providing more food options that make them feel happy instead of guilty when they eat it.
I am teaching cooking classes to promote my products as well as doing exhibits and events. I want to give away a sticker to people that reads "I'm too sweet for sugar!" and somewhere on it would be my logo as well as my website info. www.brightplate.example
The sticker should make people smile and warm as well as draw interest to my product line.
Target Market(s)
Diabetes and people who do not want added sugars in their food
Industry/Entity Type
Food Store
Requirements
Must have
- my logo and website

```html
<!DOCTYPE html>
<html lang="en">
<head>
<meta charset="utf-8">
<title>Bright Plate – I'm too sweet for sugar sticker</title>
<link rel="stylesheet" href="https://fonts.googleapis.com/css2?family=Lobster&family=Open+Sans:wght@600&display=swap">
<style>
  :root {
    --page-bg: #ffffff;
    --ring-green: #3f9c45;
    --swirl-light: #cde8cd;
    --swirl-mid: #b3dbb3;
    --ink-purple: #5a2a88;
    --ink-purple-edge: #8c62b3;
    --ornament-green: #3f9c45;
  }
  html, body {
    margin: 0;
    padding: 0;
    width: 1000px;
    height: 1200px;
    overflow: hidden;
    background: var(--page-bg);
  }
  .sticker {
    display: block;
    width: 1000px;
    height: 1200px;
  }
  .sticker__ring {
    fill: none;
    stroke: var(--ring-green);
    stroke-width: 11;
  }
  .sticker__ornament {
    fill: var(--ornament-green);
  }
  .brand-name {
    font-family: "Lobster", cursive;
    font-size: 58px;
    fill: var(--ink-purple);
    text-anchor: middle;
  }
  .slogan {
    font-family: "Lobster", cursive;
    fill: var(--ink-purple);
    stroke: var(--ink-purple-edge);
    stroke-width: 2;
    paint-order: stroke fill;
    text-anchor: middle;
  }
  .slogan--small { font-size: 145px; letter-spacing: 6px; }
  .slogan--large { font-size: 215px; letter-spacing: 8px; }
  .website {
    font-family: "Open Sans", sans-serif;
    font-weight: 600;
    font-size: 36px;
    fill: var(--ring-green);
    letter-spacing: 0.5px;
  }
</style>
</head>
<body>
<svg class="sticker" viewBox="0 0 1000 1200" xmlns="http://www.w3.org/2000/svg">
  <defs>
    <radialGradient id="swirl-fill" cx="50%" cy="50%" r="50%">
      <stop offset="0%" stop-color="var(--swirl-light)"/>
      <stop offset="100%" stop-color="var(--swirl-mid)"/>
    </radialGradient>
    <path id="website-arc" d="M 122 571 A 378 378 0 0 0 878 571"/>
  </defs>

  <g class="sticker__background" role="img" aria-label="Soft green peppermint-candy swirl pattern">
    <circle cx="500" cy="571" r="413" fill="url(#swirl-fill)"/>
  </g>
  <circle class="sticker__ring" cx="500" cy="571" r="413"/>

  <text class="brand-name" x="500" y="290">Bright Plate</text>

  <g role="img" aria-label="Decorative green scroll flourish">
    <rect class="sticker__ornament" x="405" y="352" width="190" height="9" rx="4.5"/>
  </g>

  <text class="slogan slogan--small" x="500" y="502">I’m too</text>
  <text class="slogan slogan--large" x="500" y="665">sweet</text>
  <text class="slogan slogan--small" x="500" y="792">for sugar</text>

  <g role="img" aria-label="Decorative green scroll flourish">
    <rect class="sticker__ornament" x="405" y="862" width="190" height="9" rx="4.5"/>
  </g>

  <text class="website">
    <textPath href="#website-arc" startOffset="50%" text-anchor="middle">www.brightplate.example</textPath>
  </text>
</svg>
</body>
</html>
```